Billboard design - consider what a billboard is

Design a billboard using my logo - Billboard is 6m x 3m
A Billboard is advertising for my company that is on a big sign.

Has to be clean and easy to read, and ideally highlights that we are Residential and Commercial builders.

Keep it clean and easy to read

The contact number for the board is

022 583 7092
www.harbourframeworks.co.nz
info@harbourframeworks.co.nz

Doesnt have to have all contact details if it doesnt fit

Has to catch peoples attention to contact us if they need a builder

Can you please change the sign to be all white writing, with black background ?
Updates

Please consider what a billboard is...

The design needs to be suitable for a billboard..

Target Market(s)

people driving past

Industry/Entity Type

Construction

Logo Text

Wellington Builder, website email address, contact number

Colors
0054AA
0677BA
7BADD7
CADEEF
E8F1F8

Requirements
Must have
• Easy to read
Nice to have
• easy to read, can clearly see contact details

```html
<!DOCTYPE html>
<html lang="en">
<head>
<meta charset="utf-8">
<title>Harbour Frameworks Billboard</title>
<link rel="stylesheet" href="https://fonts.googleapis.com/css2?family=Montserrat:wght@500;700;800&display=swap">
<style>
  :root {
    --sign-blue: #5a8ac6;
    --brand-blue: #4a7dc0;
    --panel-white: #ffffff;
    --band-grey: #5f5f5f;
    --text-grey: #4a4a4a;
    --page-bg: #e9ebee;
  }
  html, body {
    margin: 0;
    padding: 0;
    overflow: hidden;
  }
  body {
    width: 1165px;
    height: 1200px;
    background: var(--page-bg);
    font-family: "Montserrat", Arial, sans-serif;
    position: relative;
  }
  .billboard {
    position: absolute;
    left: 42px;
    top: 330px;
    width: 1080px;
    height: 540px;
    background: var(--sign-blue);
    overflow: hidden;
    box-shadow: 0 18px 40px rgba(0,0,0,0.25);
  }
  .billboard-shapes {
    position: absolute;
    inset: 0;
  }
  .headline {
    position: absolute;
    left: 63px;
    top: 44px;
    margin: 0;
    color: var(--panel-white);
    font-weight: 800;
    font-size: 90px;
    line-height: 100px;
    letter-spacing: -1px;
    text-shadow: 3px 3px 0 rgba(40,60,100,0.35);
  }
  .phone {
    position: absolute;
    left: 62px;
    top: 378px;
    display: flex;
    align-items: center;
    gap: 14px;
    color: var(--text-grey);
    font-weight: 800;
    font-size: 64px;
    letter-spacing: -0.5px;
    line-height: 1;
  }
  .phone-icon {
    width: 60px;
    height: 60px;
    flex: none;
  }
  .email {
    position: absolute;
    left: 63px;
    top: 480px;
    color: var(--panel-white);
    font-weight: 500;
    font-size: 21px;
  }
  .website {
    position: absolute;
    left: 590px;
    top: 480px;
    color: var(--text-grey);
    font-weight: 500;
    font-size: 21px;
  }
  .website-mid {
    color: var(--brand-blue);
  }
  .brand-name {
    position: absolute;
    left: 700px;
    top: 300px;
    width: 340px;
    margin: 0;
    color: var(--brand-blue);
    font-weight: 800;
    font-size: 48px;
    line-height: 54px;
    text-align: center;
  }
</style>
</head>
<body>
  <section class="billboard" aria-label="Harbour Frameworks billboard">
    <svg class="billboard-shapes" width="1080" height="540" viewBox="0 0 1080 540" aria-hidden="true">
      <!-- left contact band -->
      <rect x="0" y="363" width="680" height="92" fill="var(--panel-white)"/>
      <rect x="0" y="455" width="620" height="85" fill="var(--band-grey)"/>
      <!-- diagonal divider stripe -->
      <polygon points="736,258 758,258 516,540 494,540" fill="var(--band-grey)"/>
      <!-- right brand panel -->
      <polygon points="758,258 1080,258 1080,540 516,540" fill="var(--panel-white)"/>
    </svg>

    <h1 class="headline">Residential<br>and Commercial<br>Builders</h1>

    <div class="phone">
      <svg class="phone-icon" viewBox="0 0 60 60" aria-hidden="true">
        <circle cx="30" cy="30" r="29" fill="var(--brand-blue)"/>
        <path d="M22 16c2 0 3 1 4 4l1 4c0 2-1 3-3 4 1 4 4 7 8 9 1-2 2-3 4-3l4 1c3 1 4 2 4 4v3c0 2-2 3-4 3-12 0-22-10-22-22 0-2 1-4 3-4z" fill="none" stroke="var(--panel-white)" stroke-width="2.4" stroke-linejoin="round"/>
        <path d="M33 18a10 10 0 0 1 9 9M33 12a16 16 0 0 1 15 15" fill="none" stroke="var(--panel-white)" stroke-width="2.4" stroke-linecap="round"/>
      </svg>
      <span class="phone-number">022 583 7092</span>
    </div>

    <p class="email" style="margin:0">info@harbourframeworks.co.nz</p>

    <p class="brand-name">Harbour<br>Frameworks</p>

    <p class="website" style="margin:0">www.harbour<span class="website-mid">frameworks</span>.co.nz</p>
  </section>
</body>
</html>
```